Bramwell Resources Ltd. - Refreshed business card challenge

A revised, refreshed business card design for my oil and gas company using my existing logo. Feel free to be as creative as you like!

Target Market(s)

bankers, lawyers

Industry/Entity Type

Oil And Gas Exploration

Contact Information for Business Card

See the "Must Haves" section

Font styles to use
Serif
Sans Serif

Colors

Designer to choose colors to be used in the design.

Requirements
Must have
• Existing business logo, name, title, email, phone number, business address
• Neil Hadley, CA, CPA
• Vice President Finance & Chief Financial Officer
• nhadley@bramwellresources-mail.com
• office: (587)555-0142
• cell: (403)555-0187
• 1400, 815 4 Street S.W.
• Calgary, AB
• T2P 4K8
Should not have
• Should not be plain and boring.

```html
<!DOCTYPE html>
<html lang="en">
<head>
<meta charset="utf-8">
<title>Bramwell Resources Ltd. – Business Card</title>
<link href="https://fonts.googleapis.com/css2?family=Roboto:wght@400;500;700&display=swap" rel="stylesheet">
<style>
  :root {
    --page: #ffffff;
    --ink: #3d3d3d;
    --forest: #0b4a2c;
    --forest-deep: #02462a;
    --bark: #4a2a14;
    --tab: #3c321c;
    --mist: #b7c2b5;
    --tree-faint: rgba(40, 110, 70, 0.35);
  }
  * { box-sizing: border-box; margin: 0; padding: 0; }
  html, body { width: 1200px; height: 1200px; overflow: hidden; background: var(--page); }
  body { position: relative; font-family: "Roboto", Arial, sans-serif; }

  .card {
    position: absolute;
    left: 222px;
    width: 790px;
    height: 450px;
    box-shadow: 0 6px 18px rgba(0,0,0,0.18);
    overflow: hidden;
  }
  .card--front { top: 108px; background: linear-gradient(135deg, #f4f4f4, #e9e9e9); }
  .card--back  { top: 608px; background: var(--forest-deep); }

  /* front */
  .front-tree-shade {
    position: absolute; left: 0; bottom: 0; width: 100px; height: 230px;
    background: linear-gradient(180deg, rgba(160,170,160,0.08), rgba(150,160,150,0.25));
    border-radius: 50% 50% 0 0 / 80% 80% 0 0;
  }
  .holder-name {
    position: absolute; left: 52px; top: 72px;
    font-size: 35px; font-weight: 400; letter-spacing: 0.5px; color: var(--ink);
  }
  .holder-name strong { font-weight: 700; }
  .holder-name .credentials { color: var(--forest); }
  .holder-title {
    position: absolute; left: 52px; top: 118px;
    font-size: 20px; color: var(--bark);
  }
  .contact-list { position: absolute; left: 52px; top: 221px; list-style: none; }
  .contact-item { display: flex; align-items: flex-start; height: 36px; }
  .contact-item--address { height: 64px; margin-top: 8px; }
  .contact-icon {
    width: 36px; height: 36px; flex: none;
    display: flex; align-items: center; justify-content: center;
  }
  .contact-icon--green { background: var(--forest); }
  .contact-icon--brown { background: var(--bark); }
  .contact-text {
    margin-left: 17px; font-size: 21px; line-height: 36px; color: var(--ink); white-space: nowrap;
  }
  .contact-item--address .contact-text { line-height: 28px; margin-top: 2px; }

  .brand-front {
    position: absolute; left: 535px; top: 335px;
    display: flex; align-items: center; gap: 10px;
    font-size: 40px; font-weight: 700; color: var(--forest);
  }
  .brand-mark { width: 18px; height: 18px; background: var(--forest); }

  /* back */
  .side-tab { position: absolute; top: 83px; width: 38px; height: 276px; background: var(--tab); }
  .side-tab--left { left: 0; border-radius: 0 6px 6px 0; }
  .side-tab--right { right: 0; border-radius: 6px 0 0 6px; }
  .faint-tree {
    position: absolute; bottom: 0; width: 216px;
    background: linear-gradient(180deg, rgba(40,110,70,0.15), var(--tree-faint));
    border-radius: 50% 50% 0 0 / 85% 85% 0 0;
  }
  .faint-tree--left { left: 30px; height: 345px; }
  .faint-tree--right { left: 522px; height: 320px; }
  .brand-back {
    position: absolute; left: 0; right: 0; top: 190px;
    display: flex; align-items: center; justify-content: center; gap: 14px;
    font-size: 58px; font-weight: 700; color: var(--mist);
  }
  .brand-back .brand-mark { width: 24px; height: 24px; background: var(--mist); }
</style>
</head>
<body>

<section class="card card--front">
  <div class="front-tree-shade" role="img" aria-label="Faint conifer tree silhouette"></div>

  <h1 class="holder-name"><strong>NEIL</strong> HADLEY<span class="credentials">, CA, CPA</span></h1>
  <p class="holder-title">Vice President Finance &amp; Chief Financial Officer</p>

  <ul class="contact-list">
    <li class="contact-item">
      <span class="contact-icon contact-icon--green">
        <svg width="16" height="16" viewBox="0 0 24 24"><path fill="#fff" d="M6.6 10.8a15.1 15.1 0 0 0 6.6 6.6l2.2-2.2c.3-.3.7-.4 1-.2 1.1.4 2.3.6 3.6.6.6 0 1 .4 1 1V20c0 .6-.4 1-1 1A17 17 0 0 1 3 4c0-.6.4-1 1-1h3.5c.6 0 1 .4 1 1 0 1.3.2 2.5.6 3.6.1.3 0 .7-.2 1z"/></svg>
      </span>
      <span class="contact-text">(587)555-0142</span>
    </li>
    <li class="contact-item">
      <span class="contact-icon contact-icon--brown">
        <svg width="18" height="18" viewBox="0 0 24 24"><rect x="3" y="4" width="5" height="16" rx="1" fill="#fff"/><rect x="9" y="6" width="12" height="14" rx="1" fill="#fff"/><g fill="#4a2a14"><rect x="11" y="8" width="8" height="3"/><rect x="11" y="13" width="2" height="2"/><rect x="14" y="13" width="2" height="2"/><rect x="17" y="13" width="2" height="2"/><rect x="11" y="16" width="2" height="2"/><rect x="14" y="16" width="2" height="2"/><rect x="17" y="16" width="2" height="2"/></g></svg>
      </span>
      <span class="contact-text">(403)555-0187</span>
    </li>
    <li class="contact-item">
      <span class="contact-icon contact-icon--green">
        <svg width="18" height="14" viewBox="0 0 24 18"><rect x="1" y="1" width="22" height="16" fill="#fff"/><path d="M1 1l11 9 11-9" fill="none" stroke="#0b4a2c" stroke-width="2"/></svg>
      </span>
      <span class="contact-text">nhadley@bramwellresources-mail.com</span>
    </li>
    <li class="contact-item contact-item--address">
      <span class="contact-icon contact-icon--brown">
        <svg width="14" height="18" viewBox="0 0 24 32"><path fill="#fff" d="M12 0C5.4 0 0 5.4 0 12c0 9 12 20 12 20s12-11 12-20C24 5.4 18.6 0 12 0zm0 17a5 5 0 1 1 0-10 5 5 0 0 1 0 10z"/></svg>
      </span>
      <span class="contact-text">1400, 815 4 Street S.W.<br>Calgary, AB ,T2P 4K8</span>
    </li>
  </ul>

  <div class="brand-front"><span class="brand-mark"></span>Bramwell</div>
</section>

<section class="card card--back">
  <div class="faint-tree faint-tree--left" role="img" aria-label="Faint conifer tree silhouette"></div>
  <div class="faint-tree faint-tree--right" role="img" aria-label="Faint conifer tree silhouette"></div>
  <div class="side-tab side-tab--left"></div>
  <div class="side-tab side-tab--right"></div>
  <div class="brand-back"><span class="brand-mark"></span>Bramwell</div>
</section>

</body>
</html>
```